2 menu designs: Tarn Hospitality

I have 2 restaurants that are going though large menu changes. I wanted them to have a style change as well!
-one is a steakhouse menu: must fit in two portrait legal pages. there is a picture of the menu book attached. The emphasis of the menu should be on the "steaks" and "prime rib". attached are menu items that need to be included
-the other is a burger restaurant: must fit on one legal landscape page. The focus of this menu should go to the middle of the page and emphasis "burgers" and "fries". attached is the general layout I'm interested in and the menu items that need to be included. Logo for restaurant is also included. picture of restaurant included

Both must be able to be edited often but the number of items and general placement of these items will not change

Industry/Entity Type

Hospitality

```html
<!DOCTYPE html>
<html lang="en">
<head>
<meta charset="utf-8">
<title>Beginnings &amp; Plat Du Jour Menu</title>
<link href="https://fonts.googleapis.com/css2?family=Tinos:ital,wght@0,400;0,700;1,400;1,700&display=swap" rel="stylesheet">
<style>
  :root {
    --frame: #c8742f;
    --frame-dark: #a9561c;
    --gold: #f2c055;
    --cream: #fdf5dc;
    --panel: #fdd27a;
    --red: #c0202e;
    --ink: #1d1a17;
    --white: #ffffff;
  }
  * { margin: 0; padding: 0; box-sizing: border-box; }
  html, body { width: 729px; height: 1200px; overflow: hidden; background: var(--frame); }
  body { font-family: "Tinos", "Times New Roman", serif; color: var(--ink); }
  .menu { position: relative; width: 729px; height: 1200px; background: var(--frame); }
  .ornament-band { position: absolute; left: 0; width: 729px; }
  .ornament-top { top: 0; height: 80px; background: linear-gradient(180deg, var(--frame-dark), var(--frame) 60%, var(--gold)); }
  .ornament-bottom { bottom: 0; height: 84px; background: linear-gradient(0deg, var(--frame-dark), var(--frame) 60%, var(--gold)); }
  .frame-lines { position: absolute; inset: 0; }
  .sheet {
    position: absolute; left: 50px; top: 74px; width: 629px; height: 1052px;
    background: var(--cream); border-radius: 14px;
  }
  .section-title {
    position: absolute; left: 0; top: 110px; width: 729px; text-align: center;
    color: var(--red); font-weight: 700; font-size: 24px; line-height: 28px; letter-spacing: 0.3px;
  }
  .dish { position: absolute; white-space: nowrap; }
  .dish.left { left: 83px; }
  .dish.right { left: 417px; }
  .dish-name { font-weight: 700; font-size: 12px; text-transform: uppercase; line-height: 14.5px; }
  .dish-desc { font-size: 12.5px; line-height: 14.5px; }
  .signature {
    position: absolute; left: 458px; top: 345px; width: 192px; height: 182px;
    background: var(--red); color: var(--white); text-align: center;
  }
  .signature-name { margin-top: 12px; font-size: 24px; line-height: 28.6px; text-transform: uppercase; }
  .signature-rule { width: 138px; height: 1px; background: var(--white); margin: 9px auto 0; }
  .signature-note { margin-top: 15px; font-size: 15px; line-height: 18px; letter-spacing: 0.3px; }
  .daily {
    position: absolute; left: 89px; top: 550px; width: 570px; height: 393px;
    background: var(--panel); border-radius: 12px;
  }
  .daily-title { position: absolute; left: 0; top: 12px; width: 100%; text-align: center; color: var(--red); font-weight: 400; font-size: 33px; line-height: 38px; }
  .daily-row { position: absolute; left: 0; width: 100%; white-space: nowrap; }
  .day { position: absolute; left: 0; width: 100px; text-align: center; font-weight: 700; font-size: 13px; line-height: 15px; }
  .special { position: absolute; left: 119px; }
  .special-name { font-weight: 700; font-size: 13px; text-transform: uppercase; line-height: 15px; }
  .special-desc { font-size: 12.5px; line-height: 15px; }
  .kids { position: absolute; left: 0; top: 0; width: 729px; height: 1200px; pointer-events: none; }
  .kids > * { position: absolute; left: 0; width: 729px; text-align: center; white-space: nowrap; }
  .kids-title { top: 960px; color: var(--red); font-size: 31px; line-height: 36px; font-weight: 400; }
  .kids-served { top: 996px; font-size: 18px; line-height: 24px; }
  .kids-offer { top: 1021px; color: var(--red); font-style: italic; font-weight: 700; font-size: 13px; line-height: 18px; }
  .kids-option { width: 200px !important; font-weight: 700; font-size: 11.5px; line-height: 16px; text-transform: uppercase; }
  .kids-choice { top: 1088px; font-size: 12px; line-height: 16px; text-transform: uppercase; }
</style>
</head>
<body>
<main class="menu">
  <div class="ornament-band ornament-top" role="img" aria-label="Art nouveau gold scrollwork border"></div>
  <div class="ornament-band ornament-bottom" role="img" aria-label="Art nouveau gold scrollwork border"></div>
  <svg class="frame-lines" width="729" height="1200" viewBox="0 0 729 1200" aria-hidden="true">
    <rect x="20" y="40" width="689" height="1120" rx="18" fill="none" stroke="#f2c055" stroke-width="6"/>
    <rect x="42" y="66" width="645" height="1068" rx="16" fill="#f2c055"/>
  </svg>
  <div class="sheet"></div>

  <h2 class="section-title">BEGINNINGS</h2>

  <section class="starters">
    <div class="dish left" style="top:165px"><div class="dish-name">Shrimp Louie &nbsp;$18</div><div class="dish-desc">Baby Gem Lettuce, Avocado, Little Deviled Egg</div></div>
    <div class="dish left" style="top:207px"><div class="dish-name">Lamb Ribs &nbsp;$16</div><div class="dish-desc">Chimichurri, Herbed Riatta, Feta</div></div>
    <div class="dish left" style="top:249px"><div class="dish-name">Seasonal Soup &nbsp;&nbsp;MP</div><div class="dish-desc">Markets Best, Seasonal Garnish</div></div>
    <div class="dish left" style="top:291px"><div class="dish-name">Mixed Baby Lettuces &nbsp;$9</div><div class="dish-desc">Shaved Market Vegetables, &nbsp;Lemon Herb Vinaigrette</div></div>
    <div class="dish left" style="top:332px"><div class="dish-name">Heirloom Tomatoes &nbsp;$12</div><div class="dish-desc">Buratta Cheese, Basil Essence, Red Wine Vinaigrette</div></div>
    <div class="dish left" style="top:374px"><div class="dish-name">Roasted Beets &nbsp;&nbsp;$8</div><div class="dish-desc">Soft Goat Cheese, Pistachio, Citrus Vinaigrette</div></div>
    <div class="dish left" style="top:416px"><div class="dish-name">Steakhouse Wedge &nbsp;&nbsp;$8</div><div class="dish-desc">Bouble Cut Bacon, Market Tomato,<br>Bayview Blue Cheese Dressing</div></div>
    <div class="dish left" style="top:466px"><div class="dish-name">Baby Kale Caesar $9</div><div class="dish-desc">Baby Kale, Romaine Hearts, Parmesan,<br>Garlic Brown Butter Crouton, Artichoke Caesar Vinaigrette</div></div>

    <div class="dish right" style="top:160px"><div class="dish-name">West Coast Oysters &nbsp;$18</div><div class="dish-desc">Seasonal Mignonette</div></div>
    <div class="dish right" style="top:200px"><div class="dish-name">Spiced Poached Shrimp &nbsp;$12</div><div class="dish-desc">Classic Cocktail, Green Goddess Dressing</div></div>
    <div class="dish right" style="top:242px"><div class="dish-name">Double Cute Bacon &nbsp;$8</div><div class="dish-desc">Applewood Smoked, Strap Molasses BBQ</div></div>
    <div class="dish right" style="top:284px"><div class="dish-name">Spinach Artichoke Fondue &nbsp;$8</div><div class="dish-desc">Sourdough Crouton, Harbor Spice Chips</div></div>
  </section>

  <aside class="signature">
    <div class="signature-name">Vito’s<br>Famous<br>Pop-<br>Over</div>
    <div class="signature-rule"></div>
    <div class="signature-note">COMPLIMENTARY</div>
  </aside>

  <section class="daily">
    <h2 class="daily-title">Plat Du Jour</h2>
    <div class="daily-row" style="top:66px"><div class="day">Sunday</div><div class="special"><div class="special-name">Beef Short Rib</div><div class="special-desc">24 Hour Braise, Root Vegetable Hash, Burgundy Reduction</div></div></div>
    <div class="daily-row" style="top:112px"><div class="day">Monday</div><div class="special"><div class="special-name">North Beach Cioppino</div><div class="special-desc">Shellfish And Spiced Tomato Broth, Crab Toast</div></div></div>
    <div class="daily-row" style="top:158px"><div class="day">Tuesday</div><div class="special"><div class="special-name">Sonoma Lamb T-Bone</div><div class="special-desc">Roasted Eggplant Caponata, Lamb Jus</div></div></div>
    <div class="daily-row" style="top:206px"><div class="day">Wednesday</div><div class="special"><div class="special-name">Coq Au Vin</div><div class="special-desc">Herb Roasted Breast, Red Wine Braised Thigh, Potato Puree, Root Vegetables</div></div></div>
    <div class="daily-row" style="top:256px"><div class="day">Thursday</div><div class="special"><div class="special-name">Day Boat Scallops</div><div class="special-desc">Cast Iron Seared, Creamed Sweetcorn, Herbed Lemon Citronette</div></div></div>
    <div class="daily-row" style="top:305px"><div class="day">Friday</div><div class="special"><div class="special-name">Beef Short Rib</div><div class="special-desc">24 Hour Braise, Root Vegetable Hash, Burgundy Reduction</div></div></div>
    <div class="daily-row" style="top:351px"><div class="day">Saturday</div><div class="special"><div class="special-name">North Beach Cioppino</div><div class="special-desc">Shellfish And Spiced Tomato Broth, Crab Toast</div></div></div>
  </section>

  <section class="kids">
    <div class="kids-title">KIDS $6.95</div>
    <div class="kids-served">Served with Entrée | Dessert | Drink</div>
    <div class="kids-offer">Kids under 10 EAT FREE before 7pm —up to 2 kids per each purchased adult entree</div>
    <div class="kids-option" style="left:125px;top:1048px">Chicken Tenders</div>
    <div class="kids-option" style="left:269px;top:1048px">Burger</div>
    <div class="kids-option" style="left:374px;top:1048px">Steak</div>
    <div class="kids-option" style="left:480px;top:1048px">Salmon</div>
    <div class="kids-option" style="left:124px;top:1068px">Mac &amp; Cheese</div>
    <div class="kids-option" style="left:391px;top:1068px">Seasonal Mixed Vegetables</div>
    <div class="kids-choice">Choice of Fries or Broccoli &amp; Ice Cream Sundae or Fruit</div>
  </section>
</main>
</body>
</html>
```